Health and wellnes company needs business cards

We are a Health and wellness business just relocated to Spain. Here nobody knows our business so we would like to put some of our services on the card. Clean design with logo.

Contact Information for Business Card

Brightmeadow
Clara & Tobias Wennberg
Calle de los Almendros 17
Villanueva del Mar
Mobile: 0046 731 402768
info@brightmeadow-example.se

Font styles to use
Serif

Colors
85cae6
85acd3
b768aa

Requirements
Must have
• these Services somewhere on the card
• - Private or group yoga
• - Reconnective healing
• - Kitesurfing lessons
• - Massage
• LOgo somewhere
Nice to have
• Colours that go with the logo please

```html
<!DOCTYPE html>
<html lang="en">
<head>
<meta charset="utf-8">
<title>Brightmeadow – Business Card</title>
<link rel="stylesheet" href="https://fonts.googleapis.com/css2?family=Lato:wght@400;700&display=swap">
<style>
  :root {
    --stage: #3a3a3a;
    --card: #f4f4f4;
    --navy: #1c2d5a;
    --teal: #7cc6c9;
    --shadow: rgba(0, 0, 0, 0.45);
  }
  * { box-sizing: border-box; margin: 0; padding: 0; }
  html, body {
    width: 1200px;
    height: 997px;
    overflow: hidden;
    background: var(--stage);
    font-family: "Lato", Arial, sans-serif;
    color: var(--navy);
  }
  .card {
    position: absolute;
    width: 560px;
    height: 320px;
    background: var(--card);
    border-radius: 22px;
    box-shadow: 0 18px 40px var(--shadow);
    overflow: hidden;
  }
  .card--front { left: 60px; top: 120px; }
  .card--back  { left: 580px; top: 520px; }

  /* Front */
  .front-mark {
    position: absolute;
    inset: 0;
    display: flex;
    flex-direction: column;
    align-items: center;
    justify-content: center;
    gap: 22px;
  }
  .front-mark__dot {
    width: 110px;
    height: 110px;
    border-radius: 50%;
    background: var(--teal);
  }
  .front-mark__name {
    font-size: 40px;
    font-weight: 700;
    letter-spacing: 2px;
    text-transform: uppercase;
  }

  /* Back */
  .brand {
    position: absolute;
    top: 16px;
    left: 0;
    right: 0;
    display: flex;
    flex-direction: column;
    align-items: center;
    gap: 8px;
  }
  .brand__dot {
    width: 50px;
    height: 50px;
    border-radius: 50%;
    background: var(--teal);
  }
  .brand__name {
    font-size: 26px;
    line-height: 1.1;
    font-weight: 700;
    letter-spacing: 1.5px;
    text-transform: uppercase;
  }
  .divider {
    position: absolute;
    left: 24px;
    right: 24px;
    top: 120px;
    height: 2px;
    background: var(--navy);
  }
  .contact {
    position: absolute;
    left: 30px;
    top: 134px;
    font-size: 14px;
    line-height: 1.35;
  }
  .contact__names {
    display: inline-block;
    font-weight: 700;
    font-size: 14px;
    letter-spacing: 0.5px;
    text-transform: uppercase;
    border-bottom: 2px solid var(--navy);
    padding-bottom: 3px;
    margin-bottom: 6px;
  }
  .contact__address { margin-bottom: 8px; }
  .contact__list { list-style: none; }
  .contact__item {
    display: flex;
    align-items: center;
    gap: 10px;
    margin-bottom: 3px;
  }
  .contact__item svg { width: 14px; height: 14px; flex: none; fill: var(--navy); }
  .services {
    position: absolute;
    right: 28px;
    top: 134px;
    text-align: right;
    font-size: 13px;
    line-height: 1.45;
  }
  .services__title {
    font-weight: 700;
    font-size: 14px;
    text-decoration: underline;
    text-underline-offset: 3px;
    margin-bottom: 2px;
  }
  .services__list { list-style: none; }
  .services__list li::after {
    content: "";
    display: inline-block;
    width: 5px;
    height: 5px;
    border-radius: 50%;
    background: var(--navy);
    margin-left: 6px;
    vertical-align: middle;
  }
</style>
</head>
<body>
  <section class="card card--front" aria-label="Business card front">
    <div class="front-mark">
      <span class="front-mark__dot"></span>
      <span class="front-mark__name">Brightmeadow</span>
    </div>
  </section>

  <section class="card card--back" aria-label="Business card back">
    <header class="brand">
      <span class="brand__dot"></span>
      <span class="brand__name">Brightmeadow</span>
    </header>
    <div class="divider"></div>

    <div class="contact">
      <p class="contact__names">Clara &amp; Tobias Wennberg</p>
      <p class="contact__address">Calle de los Almendros 17<br>Villanueva del Mar</p>
      <ul class="contact__list">
        <li class="contact__item">
          <svg viewBox="0 0 16 16" aria-hidden="true"><path d="M3 1h3l1.5 4-2 1.3a9 9 0 0 0 4.2 4.2L11 8.5l4 1.5v3a2 2 0 0 1-2 2A12 12 0 0 1 1 3a2 2 0 0 1 2-2z"/></svg>
          0046 731 402768
        </li>
        <li class="contact__item">
          <svg viewBox="0 0 16 16" aria-hidden="true"><path d="M1 3h14v10H1z M2 4.2v.4l6 4 6-4v-.4z" fill-rule="evenodd"/></svg>
          info@brightmeadow-example.se
        </li>
        <li class="contact__item">
          <svg viewBox="0 0 16 16" aria-hidden="true"><circle cx="8" cy="8" r="7"/><path d="M1 8h14M8 1c-3 3-3 11 0 14M8 1c3 3 3 11 0 14" stroke="#f4f4f4" stroke-width="1" fill="none"/></svg>
          www.brightmeadow-example.se
        </li>
      </ul>
    </div>

    <aside class="services">
      <p class="services__title">Our Services</p>
      <ul class="services__list">
        <li>Massage</li>
        <li>Kitesurfing lessons</li>
        <li>Reconnective healing</li>
        <li>Private or group yoga</li>
      </ul>
    </aside>
  </section>
</body>
</html>
```